Move the hackers to Wordpress

Yep, we want to move https://www.tallowmarsh.com/ to Wordpress. It'll make it easier to update and add content. I'd like mostly the same look, but I'm not stuck with it.
Updates

DO NOT RESPOND OUTSIDE OF PIXEL HARBOR OR CONTACT US DIRECTLY.

Industry/Entity Type

Computer Security

Coding

Coded - Design and coding required

Font styles to use
Sans Serif

Colors
ec1f27

Requirements
Must have
• What I do want is:
• 1. Similar look to the existing site
• 2. Needs to work on one of the Wordpress hosting sites. I do NOT want to run my own Wordpress server.
• 3. Keep the animation in the top panel.
• 4. Mobile support
• The rest can be changed as needed.
Nice to have
• I like the transitions when the "services" panel shows up. Not stuck on it, but it is a nice touch.

```html
<!DOCTYPE html>
<html lang="en">
<head>
<meta charset="utf-8">
<title>Tallow Marsh — Offensive Services</title>
<link rel="stylesheet" href="https://fonts.googleapis.com/css2?family=Roboto:wght@300;400;500;700;900&display=swap">
<style>
:root{
  --red:#ec1f27;
  --red-dark:#c7141b;
  --ink:#222;
  --dark:#1b1b1d;
  --grey:#eceaea;
  --muted:#666;
  --white:#fff;
}
*{box-sizing:border-box;margin:0;padding:0}
html,body{width:1200px;height:3100px;overflow:hidden}
body{font-family:"Roboto",Arial,sans-serif;color:var(--ink);background:var(--white);position:relative}
.hero{position:absolute;left:0;top:0;width:1200px;height:680px;background:linear-gradient(160deg,#5a5d63 0%,#3a3c40 45%,#1f2023 100%)}
.hero-photo{position:absolute;inset:0;background:radial-gradient(ellipse at 70% 60%,rgba(160,165,175,.45),transparent 60%)}
.topbar{position:absolute;left:0;top:0;width:1200px;height:70px;background:rgba(10,10,12,.55);display:flex;align-items:center;justify-content:space-between;padding:0 60px}
.brand{display:flex;align-items:center;gap:10px}
.brand-mark{width:22px;height:22px;background:var(--red)}
.brand-name{font-weight:900;font-size:24px;letter-spacing:1px;color:var(--red)}
.brand-tag{font-size:9px;color:#ccc;letter-spacing:1px;margin-top:2px}
.nav{display:flex;gap:24px;list-style:none}
.nav li{font-size:12px;color:var(--white);font-weight:500;letter-spacing:.5px}
.hero-title{position:absolute;top:330px;width:100%;text-align:center;color:var(--white);font-weight:900;font-size:50px;line-height:62px;letter-spacing:1px}
.hero-title .accent{color:var(--red)}
.band{position:absolute;left:0;width:1200px;background:var(--red);color:var(--white);text-align:center}
.band h2{font-size:44px;font-weight:700;padding-top:36px}
.intro{top:680px;height:250px}
.intro p{width:900px;margin:18px auto 0;font-size:13px;line-height:20px}
.services{position:absolute;left:0;top:930px;width:1200px;height:650px;background:var(--grey)}
.service-grid{position:absolute;left:188px;top:14px;width:824px;display:grid;grid-template-columns:repeat(3,1fr);background:var(--white);border:1px solid #ddd}
.service{height:310px;border:1px solid #e2e2e2;padding:30px 26px 0;text-align:center}
.icon{width:60px;height:60px;border-radius:50%;background:var(--red);margin:0 auto 18px;display:flex;align-items:center;justify-content:center}
.service h3{font-size:16px;font-weight:700;line-height:21px;margin-bottom:12px}
.service p{font-size:11px;line-height:16px;color:var(--muted)}
.more{display:block;margin-top:12px;font-size:12px;color:var(--red);font-weight:500}
.about{top:1580px;height:480px}
.about .sub{font-size:13px;margin-top:10px}
.video{position:absolute;left:264px;top:152px;width:672px;height:288px;background:linear-gradient(135deg,#1a1d22,#3b4656 55%,#101215)}
.play{position:absolute;left:306px;top:114px;width:60px;height:60px;border-radius:50%;background:rgba(255,255,255,.85);display:flex;align-items:center;justify-content:center}
.blogs{position:absolute;left:0;top:2060px;width:1200px;height:768px;text-align:center}
.blogs h2{font-size:46px;font-weight:900;padding-top:128px}
.blogs h2 span{color:var(--red)}
.blog-row{position:absolute;left:188px;top:212px;width:824px;display:flex;gap:4px}
.post{width:272px;text-align:left;background:var(--white);padding:0}
.post-img{height:228px}
.post h4{font-size:12px;color:var(--red);margin:12px 0 4px;font-weight:700}
.meta{font-size:10px;color:#999;margin-bottom:6px}
.post p{font-size:11px;line-height:15px;color:var(--muted);padding-right:10px}
.arrow{position:absolute;top:410px;width:30px;height:30px;border-radius:50%;background:var(--red);display:flex;align-items:center;justify-content:center}
.btn{position:absolute;left:517px;top:690px;width:166px;height:40px;background:var(--red);color:var(--white);font-size:13px;font-weight:700;line-height:40px;text-align:center}
.footer{position:absolute;left:0;top:2828px;width:1200px;height:272px;background:var(--dark);color:#ccc}
.fcol{position:absolute;top:76px}
.fcol h5{font-size:18px;color:var(--white);font-weight:700;margin-bottom:12px}
.fcol h5 span{color:var(--red)}
.fcol li{list-style:none;font-size:12px;line-height:20px}
.foot-tag{font-size:16px;font-weight:700;color:var(--white);line-height:20px;margin-top:10px}
.subscribe{display:flex;margin-top:6px}
.subscribe .field{width:160px;height:32px;background:var(--white);font-size:11px;color:#999;padding:9px}
.subscribe .go{width:90px;height:32px;background:var(--red);color:var(--white);font-size:11px;font-weight:700;line-height:32px;text-align:center}
.social{position:absolute;left:530px;top:212px;display:flex;gap:12px}
.social i{width:24px;height:24px;border-radius:50%;background:var(--red);display:block}
</style>
</head>
<body>

<header class="hero">
  <div class="hero-photo" role="img" aria-label="Dim photo of hands typing on a laptop keyboard"></div>
  <div class="topbar">
    <div>
      <div class="brand"><span class="brand-mark"></span><span class="brand-name">TALLOW MARSH</span></div>
      <div class="brand-tag">INFORMATION SECURITY CONSULTING</div>
    </div>
    <ul class="nav"><li>ABOUT US</li><li>BLOG</li><li>EMAIL</li><li>SERVICES</li></ul>
  </div>
  <h1 class="hero-title"><span class="accent">OFFENSIVE</span> SERVICES<br>FROM <span class="accent">OFFENSIVE</span> MINDS</h1>
</header>

<section class="band intro">
  <h2>What We Do</h2>
  <p>Tallow Marsh is an information security consulting company that concentrates on the latest threats your organization faces. We perform in-depth testing to find weaknesses before attackers do, and then work with your team to fix them. Our consultants have tested systems for financial institutions, health providers, manufacturers, retailers and government agencies across the country.</p>
</section>

<section class="services">
  <div class="service-grid">
    <article class="service">
      <div class="icon"><svg width="28" height="28" viewBox="0 0 28 28"><path d="M8 6h12M8 22h12M9 6l8 8-8 8" fill="none" stroke="#fff" stroke-width="2.5"/></svg></div>
      <h3>Internal Pivot Assessment &amp; Post Exploitation</h3>
      <p>We start as a low-privilege user and attempt to move through the network to an objective, showing how far an attacker could go once inside.</p>
      <span class="more">READ MORE...</span>
    </article>
    <article class="service">
      <div class="icon"><svg width="30" height="30" viewBox="0 0 30 30"><circle cx="15" cy="7" r="4" fill="#fff"/><circle cx="7" cy="22" r="4" fill="#fff"/><circle cx="23" cy="22" r="4" fill="#fff"/><path d="M15 7L7 22L23 22Z" fill="none" stroke="#fff" stroke-width="2"/></svg></div>
      <h3>Red Team Adversary Simulation</h3>
      <p>Goal-based assessments where we attack your business like a real adversary, testing people, process and technology together.</p>
      <span class="more">READ MORE...</span>
    </article>
    <article class="service">
      <div class="icon"><svg width="30" height="30" viewBox="0 0 30 30"><circle cx="15" cy="15" r="9" fill="none" stroke="#fff" stroke-width="5" stroke-dasharray="4 3"/><circle cx="15" cy="15" r="4" fill="#fff"/></svg></div>
      <h3>Internal Pivot Assessment &amp; Post Exploitation</h3>
      <p>This includes vulnerability scans of the in-scope systems and manual verification to remove false positives from the final report.</p>
      <span class="more">READ MORE...</span>
    </article>
    <article class="service">
      <div class="icon"><svg width="28" height="28" viewBox="0 0 28 28"><path d="M5 23l9-9M14 14l6-9 3 3-9 6M4 24l3 0" fill="none" stroke="#fff" stroke-width="2.5"/></svg></div>
      <h3>Advanced Product, Hardware &amp; RF Testing</h3>
      <p>A highly customized assessment designed for your product or device, covering firmware, radio traffic and physical interfaces.</p>
      <span class="more">READ MORE...</span>
    </article>
    <article class="service">
      <div class="icon"><svg width="28" height="28" viewBox="0 0 28 28"><circle cx="14" cy="14" r="10" fill="none" stroke="#fff" stroke-width="2.5"/><path d="M14 14l6-5" stroke="#fff" stroke-width="2.5"/></svg></div>
      <h3>Web Application Penetration Testing</h3>
      <p>Our team performs an in-depth analysis of your web applications to find flaws in logic, authentication, input handling and sessions.</p>
      <span class="more">READ MORE...</span>
    </article>
    <article class="service">
      <div class="icon"><svg width="24" height="30" viewBox="0 0 24 30"><rect x="4" y="2" width="16" height="26" rx="2" fill="none" stroke="#fff" stroke-width="2.5"/><circle cx="12" cy="23" r="1.5" fill="#fff"/></svg></div>
      <h3>Mobile Application Assessment</h3>
      <p>We look at your mobile application and its supporting services to find weaknesses in storage, transport and server logic.</p>
      <span class="more">READ MORE...</span>
    </article>
  </div>
</section>

<section class="band about">
  <h2>About Us</h2>
  <p class="sub">We focus on hacking. This is our passion. We find the vulnerabilities before the bad guys do.</p>
  <div class="video" role="img" aria-label="Video still of a person wearing glasses looking at a screen of code">
    <div class="play"><svg width="22" height="24" viewBox="0 0 22 24"><path d="M4 2l16 10-16 10z" fill="var(--red)"/></svg></div>
  </div>
</section>

<section class="blogs">
  <h2><span>Latest</span> Blogs</h2>
  <div class="arrow" style="left:140px"><svg width="12" height="12" viewBox="0 0 12 12"><path d="M8 1L3 6l5 5" fill="none" stroke="#fff" stroke-width="2"/></svg></div>
  <div class="arrow" style="left:1030px"><svg width="12" height="12" viewBox="0 0 12 12"><path d="M4 1l5 5-5 5" fill="none" stroke="#fff" stroke-width="2"/></svg></div>
  <div class="blog-row">
    <article class="post">
      <div class="post-img" role="img" aria-label="Screenshot of a search results page listing user names" style="background:linear-gradient(180deg,#f3f3f3,#cfd6e0)"></div>
      <h4>Gathering Users from Public Profiles</h4>
      <div class="meta">May 22, 2018 · 0 comments</div>
      <p>A quick look at how public profiles can feed a username list during early recon.</p>
      <span class="more">READ MORE...</span>
    </article>
    <article class="post">
      <div class="post-img" role="img" aria-label="Screenshot of a command prompt window" style="background:linear-gradient(180deg,#2c6fb0 0 14%,#111 14%)"></div>
      <h4>Beyond the Net — Part 2: AD Groups</h4>
      <div class="meta">May 15, 2018 · 0 comments</div>
      <p>Continuing the series with simple commands that map domain groups from a foothold.</p>
      <span class="more">READ MORE...</span>
    </article>
    <article class="post">
      <div class="post-img" role="img" aria-label="Screenshot of a phone app settings screen" style="background:linear-gradient(180deg,#e7e9ee,#b8c1cf)"></div>
      <h4>Better PSK Cracking with Word Lists</h4>
      <div class="meta">May 8, 2018 · 0 comments</div>
      <p>Tips for cracking captured wireless keys faster using rules and smarter word lists.</p>
      <span class="more">READ MORE...</span>
    </article>
  </div>
  <div class="btn">VIEW MORE</div>
</section>

<footer class="footer">
  <div class="fcol" style="left:110px">
    <div class="brand"><span class="brand-mark"></span><span class="brand-name">TALLOW MARSH</span></div>
    <p class="foot-tag"><span style="color:var(--red)">OFFENSIVE</span> SERVICES<br>FROM <span style="color:var(--red)">OFFENSIVE</span> MINDS</p>
  </div>
  <div class="fcol" style="left:440px">
    <h5><span>QUICK</span> LINK</h5>
    <ul><li>Home</li><li>About Us</li><li>Services</li><li>Contact</li></ul>
  </div>
  <div class="fcol" style="left:600px">
    <h5><span>CONTACT</span> US</h5>
    <ul><li>hello@tallowmarsh.com</li><li>+1 (555) 014-2207</li></ul>
  </div>
  <div class="fcol" style="left:820px">
    <h5><span>SUBSCRIBE</span></h5>
    <div class="subscribe"><div class="field">Email Address</div><div class="go">Subscribe</div></div>
  </div>
  <div class="social"><i></i><i></i><i></i><i></i></div>
</footer>

</body>
</html>
```